Pale Lantern Double Sided Flyer Design

We need a double sided flyer (1/3 of an A4 which is 99mm x 210mm) developed for our Newcastle(NSW) tour. This flyer will be placed in tourist information centres and hotels. We want it to direct people to our website or be able to make bookings over the phone.

About Us:-
We are a city walking tour company that runs tours day or night. We run both day and night and will incorporate real history / real Pale lantern. Some of the stories will be quite serious i.e.- there are infamous murders from 100 years ago, baffling court cases, even a bit of poetry written by murderers, suicides, love triangles, you name it. We will be telling the historical stories that tourists will not hear from any other tour provider. A bit of darkness, a bit of mystery and a bit of history theme.

We do no go for scares and let the very real stories deliver the entertainment for our guests. Our customers enjoy our tours, but it isn't light fun and frivolity. Our stories are being carefully crafted and are packed with unexpected twists, turns; revelations whilst remaining all 100% true. We deliver deep, rich, engaging stories.

Here are a few samples of quotes from the characters in our stories that may give you an idea of the kind of history we will cover:-

"There were bits of spines, bits of skulls, [and] finger bones spilled out all over the streets - I ended up filling three boxes. Children were playing with them for weeks”

"I had a close shave last night and now I want a close haircut.”

“She's a beautiful child', isn't she? She's the cause of all the trouble.”

“I did it because she would not come home with me.”

"I have killed my wife. I’m glad she’s dead.”

"Stand aside or I'll put a bullet through both of you."

“You villain, I'll teach you to take away my character."

“You’re not dead yet, you bastard!”

Our website, booking form and contact details can be viewed at www.palelantern.com.au

Target Market(s)

Tourists

Industry/Entity Type

Tour

Colors

Designer to choose colors to be used in the design.

Requirements
Must have
• Vertical orientation please.
• Please also include a reference to a discount offer of 25% using the promo code "WICK".
Nice to have
• FRONT FLYER INFORMATION
• - Pale Lantern Logo
• - "I have killed my wife; I'm glad she's dead."
• - Harbourside Hidden Lanes Walk
• - 25% Discount Offer Codeword WICK
• - web address at the base; www.palelantern.com.au
• BACK FLYER INFORMATION
• - "She's a beautiful child', isn't she? She's the cause of all the trouble.
• - Pale Lantern Logo at the base along with the web address www.palelantern.com.au
• - Blurb:- Pale lantern brings back Newcastle's hidden past, the forgotten past, the dark past that may not want to be remembered.
• Real stories from the streets around you. Discover the histories you won't hear anywhere else. The forgotten stories of yesteryear finally get a chance to be told. Through you they get to live again.
Should not have
• GENERAL
• Please do not include the phone number, email address or social media icons. We want to drive online bookings.

```html
<!DOCTYPE html>
<html lang="en">
<head>
<meta charset="utf-8">
<title>Pale Lantern – Double Sided Flyer</title>
<link rel="stylesheet" href="https://fonts.googleapis.com/css2?family=Montserrat:ital,wght@0,300;0,400;0,600;0,700;0,800;1,300&display=swap">
<style>
  :root {
    --page-bg: #e4e3e8;
    --ink-night: #1b1a2c;
    --ink-plum: #3a1a2e;
    --ink-wine: #6a1e33;
    --blood: #c8142a;
    --blood-deep: #8e0f20;
    --quote-red: #d8202f;
    --paper-white: #f1eee6;
    --frame-line: rgba(241, 238, 230, 0.75);
  }
  * { box-sizing: border-box; margin: 0; padding: 0; }
  html, body {
    width: 1200px; height: 1200px; overflow: hidden;
    background: var(--page-bg);
    font-family: "Montserrat", sans-serif;
  }
  .sheet {
    position: relative; width: 1200px; height: 1200px;
    display: flex; justify-content: center; align-items: center; gap: 80px;
  }
  .flyer {
    position: relative; width: 471px; height: 1000px; overflow: hidden;
    color: var(--paper-white);
    background: linear-gradient(180deg, var(--ink-wine) 0%, var(--ink-plum) 38%, var(--ink-night) 72%, var(--ink-night) 100%);
    box-shadow: 0 18px 40px rgba(20, 16, 30, 0.35);
  }
  .texture-cracks {
    position: absolute; left: 0; top: 0; width: 100%; height: 380px;
    background: radial-gradient(ellipse at 50% 30%, rgba(140, 50, 75, 0.55), rgba(58, 26, 46, 0) 70%);
  }
  .texture-splatter {
    position: absolute; left: 0; top: 380px; width: 100%; height: 520px;
    background: radial-gradient(ellipse at 40% 30%, rgba(150, 20, 40, 0.28), rgba(27, 26, 44, 0) 65%);
  }
  .brand-mark {
    position: absolute; left: 0; width: 100%;
    display: flex; justify-content: center; align-items: center; gap: 14px;
  }
  .brand-mark .dot {
    width: 22px; height: 22px; border-radius: 50%; background: var(--paper-white);
  }
  .brand-mark .name {
    font-weight: 600; font-size: 34px; letter-spacing: 1px; color: var(--paper-white);
  }

  /* Front */
  .front .brand-mark { top: 150px; }
  .front .quote {
    position: absolute; top: 300px; left: 40px; right: 40px; text-align: center;
    font-weight: 300; font-style: italic; font-size: 25px; line-height: 1.2;
    color: var(--quote-red);
  }
  .front .tour-title {
    position: absolute; top: 520px; left: 40px; right: 40px; text-align: center;
    line-height: 1.05;
  }
  .front .tour-title .lead { display: block; font-weight: 300; font-size: 32px; }
  .front .tour-title .bold { display: block; font-weight: 800; font-size: 46px; letter-spacing: 0.5px; }
  .front .offer-splash {
    position: absolute; top: 690px; left: 95px; width: 240px; height: 180px;
    border-radius: 48% 52% 44% 56% / 55% 45% 55% 45%;
    background: radial-gradient(circle at 50% 50%, var(--blood) 55%, var(--blood-deep) 100%);
  }
  .front .offer {
    position: absolute; top: 712px; left: 95px; width: 240px; text-align: center;
    line-height: 1;
  }
  .front .offer .pct { display: block; font-weight: 800; font-size: 54px; color: var(--paper-white); }
  .front .offer .small { display: block; font-weight: 700; font-size: 15px; color: var(--paper-white); margin-top: 4px; }
  .front .offer .code { display: block; font-weight: 800; font-size: 40px; color: var(--ink-night); margin-top: 2px; }
  .front .web {
    position: absolute; bottom: 70px; left: 0; width: 100%; text-align: center;
    font-weight: 700; font-size: 25px; letter-spacing: 1px;
  }

  /* Back */
  .back .frame {
    position: absolute; top: 22px; left: 22px; right: 22px; bottom: 80px;
    border: 1.5px solid var(--frame-line);
  }
  .back .portrait {
    position: absolute; top: 60px; left: 60px; right: 60px; height: 130px;
    background: radial-gradient(ellipse at 50% 60%, rgba(110, 40, 60, 0.6), rgba(58, 26, 46, 0) 70%);
  }
  .back .copy {
    position: absolute; top: 210px; left: 60px; right: 60px; text-align: center;
    text-transform: uppercase; font-weight: 400; font-size: 15px; line-height: 1.35;
  }
  .back .copy p { margin: 0 auto; }
  .back .rule {
    display: block; width: 62%; height: 1px; margin: 22px auto;
    background: var(--frame-line);
  }
  .back .brand-mark { top: 700px; }
  .back .web {
    position: absolute; bottom: 64px; left: 50%; transform: translateX(-50%);
    padding: 0 14px; background: var(--ink-night); white-space: nowrap;
    font-weight: 700; font-size: 25px; letter-spacing: 1px;
  }
</style>
</head>
<body>
<main class="sheet">

  <section class="flyer front" aria-label="Flyer front">
    <div class="texture-cracks" role="img" aria-label="Dark cracked-stone texture"></div>
    <div class="texture-splatter" role="img" aria-label="Blood handprints and splatter"></div>
    <div class="brand-mark"><span class="dot"></span><span class="name">Pale Lantern</span></div>
    <p class="quote">"I have killed my wife; I'm glad she's dead."</p>
    <h1 class="tour-title"><span class="lead">Harbourside Hidden</span><span class="bold">LANES WALK</span></h1>
    <div class="offer-splash" role="img" aria-label="Red blood splash behind the discount offer"></div>
    <div class="offer">
      <span class="pct">25%</span>
      <span class="small">DISCOUNT OFFER</span>
      <span class="small">CODEWORD</span>
      <span class="code">WICK</span>
    </div>
    <p class="web">www.palelantern.com.au</p>
  </section>

  <section class="flyer back" aria-label="Flyer back">
    <div class="texture-cracks" role="img" aria-label="Dark cracked-stone texture"></div>
    <div class="texture-splatter" role="img" aria-label="Faint handprints and splatter"></div>
    <div class="frame"></div>
    <div class="portrait" role="img" aria-label="Faded portrait of a young girl"></div>
    <div class="copy">
      <p>"She's a beautiful child', isn't she? She's the cause of all the trouble</p>
      <span class="rule"></span>
      <p>Pale Lantern brings back Newcastle's hidden past, the forgotten past, the dark past that may not want to be remembered</p>
      <span class="rule"></span>
      <p>Real stories from the streets around you. Discover the histories you won't hear anywhere else. The forgotten stories of yesteryear finally get a chance to be told. Through you they get to live again.</p>
    </div>
    <div class="brand-mark"><span class="dot"></span><span class="name">Pale Lantern</span></div>
    <p class="web">www.palelantern.com.au</p>
  </section>

</main>
</body>
</html>
```